CyberSecurity Company Website Design

DO NOT CONTACT US OUTSIDE OF PIXELHARBOR.EXAMPLE!

A professional 5 page website design for a cyber security and risk management company. We want to portray a serious and professional approach to online security and risk management for businesses. We want the website to be easy to navigate but with a modern style.

The website design pages my partners have reviewed and wish to emulate (without copying, of course ) are:
bramwickgroup.example, larchfieldpro.example and venmaro.example, Quilnova.example

The attached Zip file contains a very basic outline of the format we are looking for. We want a nice, modern design that reflects cyber security, securing networks, and risk management for business.

Target Market(s)

Large corporations with CyberSecurity Needs

Number of Pages Required

5+ page

Colors
ec1f27
ffffff
0293ce

Requirements
Must have
• The 5 pages we need designed are;
• Home page, Services, About Us, Careers and Contact.

```html
<!DOCTYPE html>
<html lang="en">
<head>
<meta charset="utf-8">
<title>Varken — Cyber Security and Risk Management</title>
<link rel="stylesheet" href="https://fonts.googleapis.com/css2?family=Arimo:wght@400;700&display=swap">
<style>
  :root {
    --red: #ec1f27;
    --red-dark: #c1181f;
    --blue: #0293ce;
    --grey: #cfcfcf;
    --ink: #1d1d1d;
    --heading: #4a4a4a;
    --white: #ffffff;
  }
  * { box-sizing: border-box; margin: 0; padding: 0; }
  html, body { width: 1200px; height: 1200px; overflow: hidden; background: var(--white); }
  body { font-family: "Arimo", Arial, sans-serif; color: var(--ink); position: relative; }
  .page { position: absolute; inset: 0; }

  /* sidebar */
  .sidebar { position: absolute; left: 322px; top: 0; width: 108px; height: 1200px; background: var(--red); }
  .sidebar-band { position: absolute; left: 0; width: 108px; background: var(--red-dark); }
  .sidebar-band.services { top: 328px; height: 209px; }
  .sidebar-band.careers { top: 734px; height: 242px; }
  .menu-toggle { position: absolute; left: 28px; top: 44px; }
  .nav { position: absolute; left: 0; top: 82px; width: 110px; list-style: none; }
  .nav li { border-top: 1px solid rgba(255,255,255,.3); font-size: 10px; color: var(--white); padding-left: 17px; display: flex; align-items: center; }
  .nav li:last-child { border-bottom: 1px solid rgba(255,255,255,.3); }

  /* header + hero */
  .brand { position: absolute; left: 430px; top: 10px; width: 447px; text-align: center; font-size: 18px; color: var(--red); letter-spacing: 1px; }
  .hero { position: absolute; left: 430px; top: 42px; width: 448px; height: 286px;
    background: linear-gradient(160deg, #7e8a93 0%, #b8bcc0 28%, #6b5848 55%, #4a3325 78%, #2f4a4a 100%); }
  .hero-title { position: absolute; left: 430px; top: 134px; width: 428px; text-align: center; font-size: 19px; font-weight: 700; line-height: 24px; color: var(--white); }
  .hero-title .accent { color: var(--blue); }

  .btn { position: absolute; background: var(--red); color: var(--white); font-size: 10px; display: flex; align-items: center; justify-content: center; border-bottom: 1px solid var(--red-dark); }

  /* sections */
  .section { position: absolute; left: 430px; width: 448px; }
  .section.grey { background: var(--grey); }
  .section-title { position: absolute; left: 430px; width: 430px; text-align: center; font-size: 19px; font-weight: 700; color: var(--heading); }
  .rule { position: absolute; height: 2px; background: var(--red); width: 51px; }
  .copy { position: absolute; text-align: center; font-size: 9.6px; line-height: 11.8px; }

  .career-photo { position: absolute; width: 76px; height: 76px; border-radius: 50%; }
  .career-name { position: absolute; width: 110px; text-align: center; font-size: 9.6px; font-weight: 700; }

  /* footer */
  .footer-heading { position: absolute; font-size: 13px; font-weight: 700; }
  .footer-line { position: absolute; font-size: 9.6px; white-space: nowrap; }
  .footer-icon { position: absolute; }
  .copyright { position: absolute; left: 527px; top: 1184px; font-size: 9.6px; display: flex; align-items: center; gap: 6px; }
</style>
</head>
<body>
<div class="page">

  <aside class="sidebar">
    <div class="sidebar-band services"></div>
    <div class="sidebar-band careers"></div>
    <svg class="menu-toggle" width="28" height="16" viewBox="0 0 28 16">
      <g stroke="#fff" stroke-width="1.2" fill="none">
        <line x1="0" y1="1" x2="16" y2="1"/><line x1="0" y1="8" x2="16" y2="8"/><line x1="0" y1="15" x2="16" y2="15"/>
        <polyline points="19,6 22,9 25,6"/>
      </g>
    </svg>
    <ul class="nav">
      <li style="height:40px">Homepage</li>
      <li style="height:32px">Services</li>
      <li style="height:37px">About US</li>
      <li style="height:35px">Career</li>
      <li style="height:36px">Contact</li>
    </ul>
  </aside>

  <header class="brand">VARKEN</header>

  <div class="hero" role="img" aria-label="Business people at a wooden desk working on a tablet"></div>
  <h1 class="hero-title">Cyber Security and<br>Risk <span class="accent">management Company</span></h1>
  <div class="btn" style="left:602px;top:190px;width:77px;height:24px;">Find Out More</div>

  <section class="section grey" style="top:328px;height:209px;"></section>
  <h2 class="section-title" style="top:354px;">Services</h2>
  <div class="rule" style="left:615px;top:378px;"></div>
  <p class="copy" style="left:466px;top:398px;width:364px;">We provide advanced security engineering and cybersecurity architecture solutions for the commercial sector and federal government.<br>Our security experts create customized IT solutions for private organizations that meet compliance requirements as well required federaland commercial qualifications<br>it's all about YOU, our customer, your needs and your safety.</p>
  <div class="btn" style="left:605px;top:485px;width:77px;height:25px;">Read More</div>

  <h2 class="section-title" style="top:555px;left:432px;">About Us</h2>
  <div class="rule" style="left:616px;top:581px;"></div>
  <p class="copy" style="left:466px;top:601px;width:356px;">Lorem ipsum dolor sit amet, consectetur adipisicing elit, sed do eiusmod tempor incididunt ut labore et dolore magna aliqua. Ut enim ad minim veniam, quis nos-trud exercitation ullamco laboris nisi ut aliquip ex ea commodo consequat. Duis aute irure dolor in reprehenderit in voluptate velit esse cillum dolore eu fugiat nulla pariatis et quasi architecto beatae vitae dicta sunt explicabo. Nemo enim ipsam voluptatem qui</p>
  <div class="btn" style="left:606px;top:691px;width:77px;height:26px;">Read More</div>

  <section class="section grey" style="top:734px;height:242px;"></section>
  <h2 class="section-title" style="top:756px;left:426px;">Careers</h2>
  <div class="rule" style="left:615px;top:783px;"></div>

  <div class="career-photo" style="left:475px;top:813px;background:radial-gradient(circle at 50% 45%,#b49a8a,#6b5a50 70%,#d8d4cf);" role="img" aria-label="Portrait of a team member"></div>
  <div class="career-photo" style="left:605px;top:816px;background:radial-gradient(circle at 50% 45%,#8a6e5c,#2a2a2a 65%);" role="img" aria-label="Portrait of a team member"></div>
  <div class="career-photo" style="left:737px;top:813px;background:radial-gradient(circle at 50% 45%,#d9b98a,#7a6a4a 65%,#4f5a3f);" role="img" aria-label="Portrait of a team member"></div>

  <div class="career-name" style="left:457px;top:905px;">Lorem ipsum dolor</div>
  <div class="career-name" style="left:594px;top:906px;">Lorem ipsum dolor</div>
  <div class="career-name" style="left:723px;top:905px;">Lorem ipsum dolor</div>
  <div class="btn" style="left:474px;top:922px;width:77px;height:25px;">Read More</div>
  <div class="btn" style="left:608px;top:922px;width:77px;height:25px;">Read More</div>
  <div class="btn" style="left:740px;top:922px;width:77px;height:25px;">Read More</div>

  <footer>
    <h3 class="footer-heading" style="left:469px;top:1009px;">Varken Corporate Office</h3>
    <svg class="footer-icon" style="left:467px;top:1029px;" width="16" height="24" viewBox="0 0 16 24">
      <path d="M8 1a7 7 0 0 0-7 7c0 5 7 15 7 15s7-10 7-15a7 7 0 0 0-7-7z" fill="none" stroke="#111" stroke-width="2"/>
      <circle cx="8" cy="8" r="2.5" fill="#111"/>
    </svg>
    <div class="footer-line" style="left:505px;top:1036px;">Halloway Plaza</div>
    <div class="footer-line" style="left:486px;top:1059px;">118 Marrow Lane, Suite 300</div>
    <div class="footer-line" style="left:490px;top:1082px;">Eastbrook, ST 00000</div>

    <h3 class="footer-heading" style="left:736px;top:1008px;">Contact Us on</h3>
    <svg class="footer-icon" style="left:722px;top:1030px;" width="18" height="20" viewBox="0 0 18 20">
      <path d="M3 1l4 0 2 5-2.5 2c1 2.5 2.5 4.5 5 6l2-2.3 4 2.3v4c-9 1-15.5-7-14.5-17z" fill="#111"/>
    </svg>
    <div class="footer-line" style="left:753px;top:1038px;">555-01-0142</div>
    <svg class="footer-icon" style="left:716px;top:1064px;" width="26" height="24" viewBox="0 0 26 24">
      <rect x="6" y="1" width="14" height="6" fill="none" stroke="#111" stroke-width="2"/>
      <rect x="1" y="7" width="24" height="11" rx="2" fill="#111"/>
      <rect x="6" y="14" width="14" height="9" fill="#fff" stroke="#111" stroke-width="2"/>
      <line x1="9" y1="18" x2="17" y2="18" stroke="#111"/>
    </svg>
    <div class="footer-line" style="left:750px;top:1073px;">555-010-0199</div>
    <svg class="footer-icon" style="left:716px;top:1106px;" width="19" height="14" viewBox="0 0 19 14">
      <rect x="1" y="1" width="17" height="12" fill="none" stroke="#111" stroke-width="1.5"/>
      <polyline points="1,1 9.5,8 18,1" fill="none" stroke="#111" stroke-width="1.5"/>
      <line x1="1" y1="13" x2="7" y2="7" stroke="#111" stroke-width="1.2"/>
      <line x1="18" y1="13" x2="12" y2="7" stroke="#111" stroke-width="1.2"/>
    </svg>
    <div class="footer-line" style="left:742px;top:1109px;">info@varken.example</div>

    <div class="copyright">
      <svg width="18" height="12" viewBox="0 0 18 12">
        <ellipse cx="9" cy="6" rx="8" ry="5" fill="none" stroke="#777"/>
        <path d="M12 4a3.5 3 0 1 0 0 4" fill="none" stroke="#777"/>
      </svg>
      <span>Copyrights 2018 All Rights Reserved</span>
    </div>
  </footer>

</div>
</body>
</html>
```